Catalog design merchandise 2020

We, Lenz Barkhaus GmbH, have been producing high-quality cleaning agents for professional users since 1923 and sell them all over Europe.

We need a revision of our merchandise catalog for 2020. The design should be based on our chemical catalog 2019. Please do not submit any designs with chemicals, we need a merchandise catalog !!! Content pages would also be good and not just the front cover. It is not a flyer, but a catalog with about 45-50 pages

Please submit 2-3 design suggestions.

Everything else can then be discussed in detail.

Sincerely yours
marketing department
Lenz Barkhaus GmbH

Target Market(s)

Commercial end users (e.g. building cleaners, hotels, industry) for cleaning agents

Font styles to use
Sans Serif

Colors

Designer to choose colors to be used in the design.

Requirements
Must have
• Clear structured design based on the chemistry catalog.
Nice to have
• Loosening up with full pages with pictures (e.g. cleaning car at the airport or vacuum cleaner in the hotel in use)

```html
<!DOCTYPE html>
<html lang="de">
<head>
<meta charset="utf-8">
<title>Veranto Katalog Handelsware 2020 – Seitenübersicht</title>
<link rel="stylesheet" href="https://fonts.googleapis.com/css2?family=Open+Sans:wght@300;400;600;700&family=Montserrat:wght@800;900&family=Michroma&display=swap">
<style>
  :root{
    --red:#a8141e;
    --teal:#0aa08f;
    --blue-dark:#0b3f8c;
    --blue-light:#3fb0ea;
    --ink:#3a3a3a;
    --grey:#8a8a8a;
    --line:#c8c8c8;
    --toc-blue:#1f6fb8;
    --toc-green:#4f9e2c;
    --toc-magenta:#c4126a;
    --toc-orange:#e08a12;
    --toc-red:#c8202a;
    --toc-teal:#0a9a88;
    --toc-grey:#888;
  }
  *{box-sizing:border-box;margin:0;padding:0}
  html,body{width:1200px;height:1200px;overflow:hidden;background:#fff}
  body{position:relative;font-family:"Open Sans",Arial,sans-serif;color:var(--ink)}
  .page{position:absolute;width:349px;height:492px;background:#fff;border:1px solid #cfcfcf;overflow:hidden}
  .p-cover{left:46px;top:66px}
  .p-profile{left:417px;top:66px}
  .p-contents{left:806px;top:66px}
  .p-facts{left:46px;top:592px;background:var(--teal)}
  .p-chapter{left:417px;top:592px}

  .brand{position:absolute;font-family:"Open Sans",Arial,sans-serif;font-weight:700;color:var(--red);letter-spacing:1px}
  .tab{position:absolute;top:0;width:21px;height:103px;background:var(--red);color:#fff;font-size:4px;font-weight:700}
  .tab .num{position:absolute;top:14px;width:100%;text-align:center;font-size:5px}
  .tab .label{position:absolute;top:26px;left:7px;writing-mode:vertical-rl;white-space:nowrap;font-size:3.6px;line-height:4px}
  .tab::after{content:"";position:absolute;bottom:-6px;left:0;border-left:21px solid transparent;border-top:6px solid var(--red)}
  .tab.left{left:0}
  .tab.left::after{border-left:none;border-right:21px solid transparent}
  .tab.right{right:0}

  /* cover */
  .cover-head{position:absolute;left:0;top:0;width:100%;height:79px;background:#fff}
  .cover-head .brand{right:28px;top:30px;font-size:14px}
  .cover-field{position:absolute;left:0;top:79px;width:100%;height:413px;
    background:radial-gradient(ellipse at 65% 35%,var(--blue-light) 0%,#1a78c8 40%,var(--blue-dark) 100%)}
  .cover-title{position:absolute;left:71px;top:209px;font-family:"Michroma",Arial,sans-serif;color:#fff;font-size:13px;line-height:17px;letter-spacing:.2px}
  .cover-year{position:absolute;left:62px;top:381px}

  /* profile */
  .profile-title{position:absolute;left:30px;top:14px;color:var(--red);font-weight:300;font-size:14px}
  .col{position:absolute;width:150px;font-size:5.3px;line-height:7.2px;text-align:justify;color:#555}
  .col h4{font-size:5.6px;font-weight:700;color:#333;line-height:6.8px;margin-bottom:6px;text-align:left}
  .col p{margin-bottom:7px}
  .col-a{left:30px;top:40px}
  .col-b{left:187px;top:40px}
  .impressum-title{position:absolute;left:30px;top:361px;color:var(--red);font-weight:300;font-size:14px}
  .imp{position:absolute;top:384px;width:100px;font-size:3.8px;line-height:4.9px;color:#555}
  .imp b{font-weight:700}
  .imp p{margin-bottom:5px}
  .imp-a{left:30px}.imp-b{left:134px}.imp-c{left:238px}
  .p-profile .brand.foot{left:18px;bottom:12px;font-size:6px}

  /* contents */
  .photo{position:absolute}
  .ph-1{left:0;top:10px;width:111px;height:90px;background:linear-gradient(160deg,#6d6a62,#b49a84 55%,#5f5a55)}
  .ph-2{left:117px;top:10px;width:112px;height:90px;background:linear-gradient(160deg,#9fb4c8,#2f65b0 50%,#e0b020)}
  .ph-3{left:235px;top:10px;width:113px;height:90px;background:linear-gradient(170deg,#d8dde2,#a8b4be 60%,#e0c23a)}
  .ph-4{left:0;top:106px;width:111px;height:88px;background:linear-gradient(170deg,#eef1ee,#8fb07c 45%,#3a6fa8)}
  .ph-5{left:0;top:200px;width:111px;height:89px;background:linear-gradient(170deg,#8a98a8,#d8dde4 50%,#6a7a8c)}
  .toc-title{position:absolute;left:128px;top:114px;color:var(--red);font-weight:300;font-size:25px}
  .toc{position:absolute;left:128px;top:145px;width:176px;font-size:5.4px;line-height:7.1px;color:var(--grey);font-weight:300}
  .toc .sec{display:flex;align-items:center;font-weight:700;margin-top:4px}
  .toc .sec:first-child{margin-top:0}
  .toc .sec .rule{flex:1;height:.5px;background:currentColor;margin:0 2px;opacity:.6}
  .toc .row{display:flex;justify-content:space-between}
  .c-blue{color:var(--toc-blue)}.c-green{color:var(--toc-green)}.c-mag{color:var(--toc-magenta)}
  .c-orange{color:var(--toc-orange)}.c-red{color:var(--toc-red)}.c-teal{color:var(--toc-teal)}.c-grey{color:var(--toc-grey)}
  .badges{position:absolute;left:130px;top:427px;display:flex;gap:16px;align-items:center}
  .badge{width:28px;height:28px}
  .badge.sq{background:#d8c64a}
  .badge.rect{width:18px;background:#7fb94a}
  .badge.round{border-radius:50%;background:#1f3f7a}

  /* facts */
  .facts{position:absolute;left:32px;top:176px;color:#fff}
  .fact-num{font-family:"Montserrat",Arial,sans-serif;font-weight:900;font-size:31px;line-height:31px;letter-spacing:-1px}
  .fact-text{font-weight:400;font-size:19px;line-height:22px;margin-bottom:12px}
  .p-facts .brand.foot{left:16px;bottom:12px;font-size:6px}

  /* chapter */
  .chapter-photo{position:absolute;left:0;top:0;width:100%;height:100%;
    background:linear-gradient(180deg,#eceeef 0%,#e3e5e7 40%,#7b82a8 58%,#6d6e76 70%,#8c8d92 100%)}
  .chapter-edge{position:absolute;left:0;top:0;width:6px;height:100%;background:#8a8a8a}
  .chapter-band{position:absolute;left:34px;top:259px;right:0;height:91px;background:var(--teal);border-bottom-left-radius:26px}
  .chapter-band span{position:absolute;left:25px;top:33px;font-family:"Montserrat",Arial,sans-serif;font-weight:800;color:#fff;font-size:15px;letter-spacing:.2px}
  .p-chapter .brand.foot{right:30px;bottom:12px;font-size:6px}
</style>
</head>
<body>

<section class="page p-cover">
  <div class="cover-head"><span class="brand">VERANTO</span></div>
  <div class="cover-field"></div>
  <h1 class="cover-title">REINIGUNGSSYSTEME,<br>HILFSMITTEL, MASCHINEN</h1>
  <svg class="cover-year" width="200" height="130" viewBox="0 0 200 130" style="top:266px;left:22px">
    <circle cx="96" cy="64" r="62" fill="none" stroke="#8fd0f5" stroke-width="1" opacity=".6"/>
    <circle cx="96" cy="64" r="57" fill="none" stroke="#bfe6fb" stroke-width="2" opacity=".8"/>
    <circle cx="96" cy="64" r="51" fill="#fff"/>
    <circle cx="96" cy="64" r="48" fill="var(--red)"/>
    <text x="96" y="76" text-anchor="middle" fill="#fff" font-family="Open Sans, Arial, sans-serif" font-size="32"><tspan font-weight="300">20</tspan><tspan font-family="Montserrat, Arial, sans-serif" font-weight="900">20</tspan></text>
  </svg>
</section>

<section class="page p-profile">
  <div class="tab left"><span class="num">2</span><span class="label">Katalogdesign Handelsware<br>2020</span></div>
  <h2 class="profile-title">Unternehmensprofil</h2>
  <div class="col col-a">
    <h4>Urgestein der Reinigungsbranche – über 90 Jahre Tradition und Erfahrung</h4>
    <p>Seit 1923 stellt die Lenz Barkhaus GmbH Reinigungsmittel für gewerbliche Anwender her. Aus einer kleinen Werkstatt entstand ein Familienbetrieb, der heute Kunden in ganz Europa beliefert. Unser Sortiment umfasst Pflegemittel, Reinigungsgeräte, Wagen und Maschinen für Gebäude, Hotels und Industrie. Mehrere Tochtergesellschaften sorgen für kurze Wege zu unseren Kunden.</p>
    <p>Im Jahr 1970 übernahm die zweite Generation die Leitung und verlegte den Sitz in ein neues Werk. Das Produktportfolio wuchs stetig, neue Standorte kamen hinzu. Heute leitet bereits die vierte Generation das Unternehmen und setzt auf Qualität, Beratung und Nähe zum Kunden.</p>
    <p>Großverbraucher werden im Inland und in der EU mit eigenem Werksfernverkehr beliefert. Die Verkaufspalette ist inzwischen durch Hilfsmittel, Gerätewagen und Maschinen erweitert worden, sodass alles aus einer Hand kommt.</p>
    <h4>Unser Bestreben</h4>
    <p>Mit unserer Vielfalt an Spezialreinigungsmitteln und Maschinen bieten wir Ihnen die komplette Lösung für Sauberkeit und Hygiene. Geschulte Fachberater betreuen Sie vor Ort, und in regelmäßigen Seminaren teilen wir unser Wissen mit Ihnen.</p>
  </div>
  <div class="col col-b">
    <h4>Der Umwelt verpflichtet</h4>
    <p>Die Lenz Barkhaus GmbH ist Mitglied mehrerer Forschungsgemeinschaften und Fachverbände. Alle Rezepturen entstehen im eigenen Haus und sind frei von FCKW, chlorierten Kohlenwasserstoffen und aromatischen Lösemitteln. Wo immer möglich, setzen wir nachwachsende Rohstoffe ein.</p>
    <p>Darüber hinaus entsprechen alle Reinigungsmittel den gesetzlichen Regelungen nach EU-Richtlinien, dem Wasch- und Reinigungsmittelgesetz, dem Chemikaliengesetz und der Gefahrstoffverordnung. Gefährdungen der Gesundheit sind bei sachgemäßer Anwendung ausgeschlossen.</p>
    <p>Wo es möglich ist, gehen wir über die gesetzlichen Vorgaben hinaus und bieten Produkte mit maximaler Umweltverträglichkeit sowie Anwenderschutz an. Viele unserer Produkte tragen anerkannte Umweltzeichen, unsere Desinfektionsmittel sind in den einschlägigen Listen geführt.</p>
    <p>Kontaktieren Sie uns, wir beraten Sie gerne!</p>
    <p>Ihre Lenz Barkhaus GmbH</p>
  </div>
  <h2 class="impressum-title">Impressum</h2>
  <div class="imp imp-a">
    <p><b>Herausgeber:</b><br>Lenz Barkhaus GmbH<br>Werkstraße 12<br>90000 Musterstadt<br>Tel. 0000 000000<br>E-Mail: info@barkhaus-beispiel.de</p>
    <p>Registergericht Musterstadt</p>
    <p>Redaktion: Marketing<br>Design und Layout: Agentur<br>Stand: April 2018</p>
  </div>
  <div class="imp imp-b">
    <p><b>Tochtergesellschaften:</b><br>Berlin<br>Lenz Barkhaus GmbH<br>Vertrieb Berlin<br>Beispielstraße 5<br>10000 Berlin<br>Tel. 0000 000000</p>
    <p>Leipzig<br>Lenz Barkhaus GmbH<br>Vertrieb Leipzig<br>Hauptstraße 8<br>04000 Leipzig<br>Tel. 0000 000000</p>
  </div>
  <div class="imp imp-c">
    <p>Braunschweig<br>Vertrieb Braunschweig<br>Marktweg 3<br>38000 Braunschweig<br>Tel. 0000 000000</p>
    <p>Frankfurt<br>Vertrieb Frankfurt<br>Ringstraße 9<br>60000 Frankfurt<br>Tel. 0000 000000</p>
  </div>
  <span class="brand foot">VERANTO</span>
</section>

<section class="page p-contents">
  <div class="photo ph-1" role="img" aria-label="Foto: Firmenvertreter mit Reinigungsflasche im Lager"></div>
  <div class="photo ph-2" role="img" aria-label="Foto: Reinigungswagen und Eimer im Ausstellungsraum"></div>
  <div class="photo ph-3" role="img" aria-label="Foto: Verkaufsraum mit Regalen"></div>
  <div class="photo ph-4" role="img" aria-label="Foto: Reinigungswagen mit Pflanzen"></div>
  <div class="photo ph-5" role="img" aria-label="Foto: Hochregallager"></div>
  <h2 class="toc-title">Inhalt</h2>
  <div class="toc">
    <div class="sec c-blue">WISCHSYSTEME<span class="rule"></span>7</div>
    <div class="row"><span>Glasreinigung</span><span>8</span></div>
    <div class="row"><span>Feuchtwischsysteme</span><span>9</span></div>
    <div class="row"><span>Spezialnasswischsysteme</span><span>10</span></div>
    <div class="row"><span>Nasswischsysteme/-wagen – Einfachfahrwagen</span><span>12</span></div>
    <div class="row"><span>Nasswischsysteme/-wagen – Doppelfahrwagen</span><span>14</span></div>
    <div class="row"><span>Nasswischsysteme/-wagen – Fahrelmer</span><span>16</span></div>
    <div class="sec c-green">HILFSGERÄTE &amp; ZUBEHÖR REIN<span class="rule"></span>17</div>
    <div class="row"><span>Tücher, Schwämme, Pads</span><span>18</span></div>
    <div class="row"><span>Kunststoffeimer &amp; Säcke</span><span>19</span></div>
    <div class="row"><span>Bürsten &amp; Besen</span><span>20</span></div>
    <div class="row"><span>sonstiges Zubehör</span><span>22</span></div>
    <div class="sec c-mag">HILFSGERÄTE &amp; ZUBEHÖR SANITÄR<span class="rule"></span>23</div>
    <div class="row"><span>Hygienepapier &amp; Spender</span><span>24</span></div>
    <div class="row"><span>Seifenspender</span><span>25</span></div>
    <div class="row"><span>sonstiges Zubehör</span><span>26</span></div>
    <div class="sec c-orange">REINIGUNGS- &amp; HOTELWAGEN<span class="rule"></span>27</div>
    <div class="sec c-red">SAUGER<span class="rule"></span>33</div>
    <div class="row"><span>Staubsauger</span><span>34</span></div>
    <div class="row"><span>Staub- &amp; Wassersauger</span><span>36</span></div>
    <div class="row"><span>Bürst- &amp; Rucksacksauger</span><span>38</span></div>
    <div class="row"><span>Zubehör Staubsauger</span><span>39</span></div>
    <div class="sec c-teal">REINIGUNGSMASCHINEN<span class="rule"></span>41</div>
    <div class="row"><span>Einscheibenmaschinen</span><span>42</span></div>
    <div class="row"><span>Sprühextraktionsgeräte</span><span>44</span></div>
    <div class="row"><span>Schrubbautomaten</span><span>45</span></div>
    <div class="sec c-grey">QR-CODES IM KATALOG<span class="rule"></span>4</div>
    <div class="row"><span>Produktverzeichnis</span><span>5</span></div>
    <div class="row"><span>Materialübersicht Wischbezüge</span><span>47</span></div>
    <div class="row"><span>Vertriebsnetz</span><span>48</span></div>
    <div class="row"><span>Allgemeine Geschäftsbedingungen</span><span>49</span></div>
    <div class="row"><span>Stichwortverzeichnis</span><span>51</span></div>
  </div>
  <div class="badges">
    <span class="badge sq"></span>
    <span class="badge rect"></span>
    <span class="badge round"></span>
    <span class="badge round"></span>
  </div>
</section>

<section class="page p-facts">
  <div class="tab left"><span class="num">4</span><span class="label">Katalogdesign Handelsware<br>2020</span></div>
  <div class="facts">
    <div class="fact-num">60</div>
    <div class="fact-text">Quis autem</div>
    <div class="fact-num">30</div>
    <div class="fact-text">Voluptatem sequi nesciunt</div>
    <div class="fact-num">12</div>
    <div class="fact-text">Quis autem vel eum</div>
  </div>
  <span class="brand foot">VERANTO</span>
</section>

<section class="page p-chapter">
  <div class="chapter-photo" role="img" aria-label="Foto: Reinigungskraft wischt einen Fliesenboden im Wartebereich mit Stuhlreihe"></div>
  <div class="chapter-edge"></div>
  <div class="tab right"><span class="num">5</span><span class="label">Katalogdesign Handelsware<br>2020</span></div>
  <div class="chapter-band"><span>WISCHSYSTEME</span></div>
  <span class="brand foot">VERANTO</span>
</section>

</body>
</html>
```